Law Firm in Texas in need of new letterhead

Law Firm in Fort Worth, TX, USA named "Vale & Brennick, Attorneys-At-Law, LLP." This is a general practice law firm that mostly does Family Law and Criminal Defense work.

We are looking for a new letterhead that has a "classical" appeal, with modern elements.

Any color combination is fine, but please note that we do fax many documents, so the design must be clearly legible in Black and White.

We would like our letterhead to project a sense of professionalism, integrity, and ability.

Target Market(s)

Letterhead will be for correspondence generally with other attorneys and clients.

Industry/Entity Type

Law Firm

Logo Text

Vale & Brennick, Attorneys-At-Law, LLP.

Logo styles of interest
Pictorial/Combination Logo
Wordmark Logo
Lettermark Logo
Requirements
Nice to have
• Although not necessary, a "Texas Star" that is incorporated into the design would be a nice touch.
Should not have
• Colors that do not convert to B&W easily

```html
<!DOCTYPE html>
<html lang="en">
<head>
<meta charset="utf-8">
<title>Vale &amp; Brennick Letterhead</title>
<link rel="stylesheet" href="https://fonts.googleapis.com/css2?family=Montserrat:wght@400;700&family=Arimo:wght@400&display=swap">
<style>
  :root {
    --backdrop: #d9d9d9;
    --paper: #ffffff;
    --ink: #1a1a1a;
  }
  html, body { margin: 0; padding: 0; overflow: hidden; }
  body { width: 1200px; height: 900px; background: var(--backdrop); position: relative; }

  .letterhead {
    --brand: #1b2a78;
    --accent: #e1141f;
    --sign: #1f3bd1;
    position: absolute; top: 86px; width: 513px; height: 728px;
    background: var(--paper); box-shadow: 0 2px 10px rgba(0,0,0,.25);
    overflow: hidden; color: var(--ink);
  }
  .letterhead--color { left: 72px; }
  .letterhead--mono { left: 615px; --brand: #1f1c1d; --accent: #1f1c1d; --sign: #1f1c1d; }

  .firm-name {
    position: absolute; top: 40px; left: 0; right: 0; margin: 0; text-align: center;
    font: 400 17px/1.2 "Arimo", sans-serif; color: var(--ink);
  }

  .letter-body {
    position: absolute; top: 242px; left: 73px; width: 372px;
    font: 400 10.7px/11.6px "Arimo", sans-serif;
  }
  .letter-body p { margin: 0 0 11.6px; }

  .signature {
    position: absolute; top: 542px; left: 68px; width: 132px; height: 22px;
    background: linear-gradient(90deg, var(--sign), rgba(255,255,255,0));
    opacity: .35; border-radius: 11px;
  }
  .signer-title {
    position: absolute; top: 568px; left: 73px; font: 400 10.7px/1 "Arimo", sans-serif;
  }

  .star-emblem {
    position: absolute; top: 582px; left: 226px; width: 58px; height: 58px;
    background: var(--brand);
  }
  .partners {
    position: absolute; top: 584px; left: 296px; width: 200px;
    font: 400 5.8px/6.8px "Montserrat", sans-serif; color: #444;
  }
  .partners p { margin: 0 0 6.8px; }

  .footer-address {
    position: absolute; top: 678px; left: 73px; font: 400 6.4px/9px "Montserrat", sans-serif;
  }
  .footer-address strong { font-weight: 700; }

  .footer-band { position: absolute; left: 0; bottom: 0; width: 513px; height: 72px; }
  .footer-contact {
    position: absolute; bottom: 8px; left: 73px; color: #fff;
    font: 400 6.4px/1 "Montserrat", sans-serif;
  }
  .footer-contact b { font-weight: 700; }
</style>
</head>
<body>

<section class="letterhead letterhead--color">
  <h1 class="firm-name">Vale &amp; Brennick, Attorneys-At-Law, LLP.</h1>

  <div class="letter-body">
    <p>Letterhead samples are a great way of deciding what kind of letterhead you want to design for you and your company. The internet has a ton of great letterhead samples to browse through. Whether you want something simple, with just a couple lines of text of your business information, or something decorative and stunning, with photos and logos on the top and bottom of the page, it will be easy to find what you want, because there are samples online for basically any type of letterhead you could want.</p>
    <p>Any business could easily benefit from browsing through some letterhead samples, if only to get an idea for what kind of letterhead their company might want. Letterheads are just one of the tools that a business professional could use to help increase their customer base, and to really be memorable to everyone they write a letter to. Letterhead is quite an effective tool for marketing and advertising, but because it’s such a simple and well known idea, it is often unfairly overlooked. Make sure you don’t make that mistake, and make some letterhead samples of your own today.</p>
    <p>Whether you want to get new customers to remember you and become part of your clientele, or you just want to send out friendly reminders to your existing clients, customizing your own letterhead samples can really help you out. Try out some letterhead samples and you will not regret it, and I’m sure you will add a new tool to your business’ arsenal of networking, marketing, and advertising tools.</p>
  </div>

  <div class="signature" role="img" aria-label="Handwritten signature of the company director"></div>
  <div class="signer-title">company director</div>

  <div class="star-emblem" role="img" aria-label="Texas star emblem"></div>
  <div class="partners">
    <p>Partners:<br>Marcus Vale, Managing Partner (Licensed in State of Texas, United States District Court (Northern District of Texas), United States Supreme Court)</p>
    <p>Dana Lee Brennick (Licensed in the State of Texas)</p>
  </div>

  <div class="footer-address"><strong>Vale &amp; Brennick, Attorneys-at-Law, LP</strong><br>1420 W. Magnolia Ave. Fort Worth, TX 76104</div>

  <svg class="footer-band" viewBox="0 0 513 72" aria-hidden="true">
    <rect x="240" y="28" width="273" height="17" fill="var(--brand)" role="img" aria-label="Fort Worth city skyline silhouette"/>
    <polygon points="0,45 238,45 226,72 0,72" fill="var(--accent)"/>
    <polygon points="240,45 513,45 513,72 228,72" fill="var(--brand)"/>
  </svg>
  <div class="footer-contact"><b>P</b> (817) 555-0142 | <b>F</b> (817) 555-0198</div>
</section>

<section class="letterhead letterhead--mono">
  <h1 class="firm-name">Vale &amp; Brennick, Attorneys-At-Law, LLP.</h1>

  <div class="letter-body">
    <p>Letterhead samples are a great way of deciding what kind of letterhead you want to design for you and your company. The internet has a ton of great letterhead samples to browse through. Whether you want something simple, with just a couple lines of text of your business information, or something decorative and stunning, with photos and logos on the top and bottom of the page, it will be easy to find what you want, because there are samples online for basically any type of letterhead you could want.</p>
    <p>Any business could easily benefit from browsing through some letterhead samples, if only to get an idea for what kind of letterhead their company might want. Letterheads are just one of the tools that a business professional could use to help increase their customer base, and to really be memorable to everyone they write a letter to. Letterhead is quite an effective tool for marketing and advertising, but because it’s such a simple and well known idea, it is often unfairly overlooked. Make sure you don’t make that mistake, and make some letterhead samples of your own today.</p>
    <p>Whether you want to get new customers to remember you and become part of your clientele, or you just want to send out friendly reminders to your existing clients, customizing your own letterhead samples can really help you out. Try out some letterhead samples and you will not regret it, and I’m sure you will add a new tool to your business’ arsenal of networking, marketing, and advertising tools.</p>
  </div>

  <div class="signature" role="img" aria-label="Handwritten signature of the company director"></div>
  <div class="signer-title">company director</div>

  <div class="star-emblem" role="img" aria-label="Texas star emblem"></div>
  <div class="partners">
    <p>Partners:<br>Marcus Vale, Managing Partner (Licensed in State of Texas, United States District Court (Northern District of Texas), United States Supreme Court)</p>
    <p>Dana Lee Brennick (Licensed in the State of Texas)</p>
  </div>

  <div class="footer-address"><strong>Vale &amp; Brennick, Attorneys-at-Law, LP</strong><br>1420 W. Magnolia Ave. Fort Worth, TX 76104</div>

  <svg class="footer-band" viewBox="0 0 513 72" aria-hidden="true">
    <rect x="240" y="28" width="273" height="17" fill="var(--brand)" role="img" aria-label="Fort Worth city skyline silhouette"/>
    <polygon points="0,45 238,45 226,72 0,72" fill="var(--accent)"/>
    <polygon points="240,45 513,45 513,72 228,72" fill="var(--brand)"/>
  </svg>
  <div class="footer-contact"><b>P</b> (817) 555-0142 | <b>F</b> (817) 555-0198</div>
</section>

</body>
</html>
```